Brume d'Orvelle Hand Crafted Candles promotional flyer

Hand Crafted Soy Candles - I need a flyer to promote my candles and to give information on care of candles.I want this to use the design and colours I already have for my labels and the photo I have attached.I am aiming at a sophisticated market so would like to reflect this in the design.
Should appeal to sophisticated women who enjoy the pleasure of candles - to enhance their enjoyment of life - gives them the 'brume d'orvelle'.
the candles are hand crafted from all natural ingredients, environmentally friendly and with exquisite fragrances

Target Market(s)

sophisticated females

Industry/Entity Type

Promotional

Font styles to use
Script

Colors
cfeae6
ecdaeb

Requirements
Must have
• something expressing 'brume d'orvelle' - the enjoyment of candles
Should not have
• bright colours

```html
<!DOCTYPE html>
<html lang="en">
<head>
<meta charset="utf-8">
<title>Brume d'Orvelle Hand Crafted Candles</title>
<link href="https://fonts.googleapis.com/css2?family=Italianno&family=Cormorant+SC:wght@500&display=swap" rel="stylesheet">
<style>
  :root {
    --lilac: #ecdaeb;
    --mint: #cfeae6;
    --teal: #86cfc0;
    --teal-deep: #5fbba9;
    --ink-plum: #5a5264;
    --slate: #34332f;
    --slate-dark: #232220;
    --text-light: #e4e0e3;
    --rule: #b7a9b6;
    --photo-dark: #1c1b22;
    --photo-label: #dfe3e8;
  }
  * { margin: 0; padding: 0; box-sizing: border-box; }
  html, body { width: 850px; height: 1200px; overflow: hidden; background: #fff; }
  .flyer {
    position: relative; width: 850px; height: 1200px; overflow: hidden;
    font-family: "Italianno", cursive;
  }
  .backdrop { position: absolute; inset: 0; }

  .hero-photo {
    position: absolute; left: 100px; top: 28px; width: 195px; height: 225px;
    border-radius: 10px 10px 16px 16px;
    background: radial-gradient(ellipse at 50% 45%, var(--photo-label) 0 33%, transparent 34%),
                linear-gradient(100deg, #2a2932, var(--photo-dark) 55%, #34333c);
  }

  .hero-points {
    position: absolute; left: 405px; top: 92px; width: 380px;
    list-style: none; color: var(--ink-plum);
    font-size: 31px; line-height: 24px;
  }
  .hero-points li { position: relative; padding-left: 16px; margin-bottom: 6px; }
  .hero-points li::before {
    content: ""; position: absolute; left: 0; top: 9px;
    width: 6px; height: 6px; border-radius: 50%; background: var(--ink-plum);
  }

  .section-title {
    color: var(--text-light); font-size: 30px; line-height: 26px;
    padding: 0 0 4px 20px; border-bottom: 1px solid var(--rule);
  }
  .info-list { list-style: none; color: var(--text-light); font-size: 16.5px; line-height: 13.5px; }
  .info-list li { position: relative; padding-left: 22px; margin-top: 10px; }
  .info-list li::before {
    content: ""; position: absolute; left: 4px; top: 4px;
    width: 6px; height: 6px; border-radius: 50%; background: #8d8a88;
  }

  .soy-column { position: absolute; left: 70px; top: 540px; width: 290px; }
  .soy-column .section-title + .info-list { margin-top: 8px; }
  .refill-title { margin-top: 24px; }

  .contact {
    position: absolute; left: 70px; top: 920px; width: 240px;
    color: var(--text-light); border-top: 1px solid var(--rule); padding-top: 6px;
  }
  .contact-intro { font-size: 19px; line-height: 15px; padding-left: 4px; }
  .contact-lines { font-size: 23px; line-height: 18px; margin-top: 10px; padding-left: 4px; }

  .care-column { position: absolute; left: 438px; top: 540px; width: 345px; }
  .care-column .section-title { text-align: center; padding-left: 0; font-size: 27px; line-height: 20px; padding-bottom: 6px; }
  .care-column .info-list { font-size: 15.5px; line-height: 13px; }

  .base-rule { position: absolute; left: 72px; top: 1045px; width: 710px; border-top: 1px solid var(--rule); }

  .brand-seal {
    position: absolute; left: 72px; top: 1072px; width: 88px; height: 88px;
    border-radius: 50%; background: var(--photo-label);
    display: flex; align-items: center; justify-content: center; text-align: center;
    font-size: 19px; line-height: 16px; color: var(--ink-plum);
  }
  .range-photo {
    position: absolute; left: 268px; top: 1076px; width: 500px; height: 84px;
    border-radius: 50% 50% 4px 4px / 30% 30% 4px 4px;
    background: linear-gradient(180deg, #3f3e42 0%, #1d1c20 100%);
  }
</style>
</head>
<body>
<main class="flyer">
  <svg class="backdrop" width="850" height="1200" viewBox="0 0 850 1200" aria-hidden="true">
    <defs>
      <linearGradient id="sky" x1="0" y1="0" x2="0" y2="1">
        <stop offset="0" stop-color="#e4cde3"/>
        <stop offset="1" stop-color="#ffffff"/>
      </linearGradient>
      <linearGradient id="slate" x1="0" y1="0" x2="1" y2="1">
        <stop offset="0" stop-color="#3d3b37"/>
        <stop offset="0.5" stop-color="#2f2e2b"/>
        <stop offset="1" stop-color="#242321"/>
      </linearGradient>
    </defs>
    <rect width="850" height="480" fill="url(#sky)"/>
    <path d="M300 40 C420 20 520 90 600 60 C680 30 760 20 850 40 L850 120 C760 80 700 130 620 120 C520 110 450 80 300 40Z" fill="#ffffff" opacity="0.55"/>
    <path d="M0 330 C140 270 260 340 400 300 C520 265 560 170 660 110 C730 70 790 60 850 70 L850 470 L0 470Z" fill="var(--mint)"/>
    <path d="M0 300 C160 250 260 320 390 285 C500 255 560 200 640 210 C720 220 780 170 850 150 L850 470 L0 470Z" fill="var(--teal)" opacity="0.75"/>
    <path d="M0 360 C120 320 250 380 380 350 C500 320 600 250 700 270 C770 285 810 260 850 250 L850 470 L0 470Z" fill="var(--teal-deep)" opacity="0.55"/>
    <path d="M0 390 C160 350 260 410 420 390 C560 372 640 320 850 330 L850 470 L0 470Z" fill="#ffffff" opacity="0.5"/>
    <path d="M0 470 C120 430 220 480 340 465 C470 450 540 520 660 500 C750 485 800 440 850 432 L850 1200 L0 1200Z" fill="url(#slate)"/>
  </svg>

  <div class="hero-photo" role="img" aria-label="Photo of a black glass candle jar with an oval Brume d'Orvelle label"></div>

  <ul class="hero-points">
    <li>Brume d'Orvelle – an exuberant enjoyment of life – these candles will fill you with "Brume d'Orvelle"</li>
    <li>Candles are lovingly hand-poured and use only the finest of ingredients and fragrances</li>
    <li>Hand crafted soy candle creations</li>
    <li>Completely non-toxic</li>
    <li>Exquisite fragrances</li>
    <li>Clean burning</li>
    <li>Environmentally friendly</li>
  </ul>

  <section class="soy-column">
    <h2 class="section-title">Why soy wax?</h2>
    <ul class="info-list">
      <li>Soft smooth wax that burns clear – no soot or smoke</li>
      <li>Soy wax candles burn up to 50% longer than traditional paraffin candles</li>
      <li>Made from soya beans, a renewable natural resource that supports and sustains agriculture – it is biodegradable and environmentally friendly</li>
      <li>Soy wax burns cooler than paraffin and disperses the fragrance more fully</li>
    </ul>
    <h2 class="section-title refill-title">Containers can be refilled</h2>
    <ul class="info-list">
      <li>I offer a refill service – if you return your containers to me I can refill with the fragrance of your choice</li>
      <li>Or if you have a special container you would like to use for your candle just contact me for a quote</li>
    </ul>
  </section>

  <address class="contact">
    <p class="contact-intro">I have a wide range of fragrances – please contact me for details:</p>
    <p class="contact-lines">Email: claire.ashby@mailbox.co.nz<br>Mobile: 021 555 0187<br>Website: www.mybrumedorvelle.co.nz</p>
  </address>

  <section class="care-column">
    <h2 class="section-title">How to care for your candle – the following tips will ensure you have a long lasting, fully fragranced candle</h2>
    <ul class="info-list">
      <li>When lighting your candle for the first time, allow the wax to melt all the way to the sides of the container – this creates a 'memory' and avoids 'tunnelling' as the candle burns</li>
      <li>Always trim the wick to about 6-8mm before re-lighting your candle. This will ensure a long lasting candle, minimise soot and remove any mushrooming of the wick from a previous burn</li>
      <li>It is preferable to use a candle 'snuffer' to extinguish the flame, or a lid if the candle has one. Alternatively, you can dip the wick into the melted wax and then straighten it. This will stop the wick from smoking and help with relighting</li>
      <li>All Brume d'Orvelle candles are hand poured not mass produced – although every effort is made to ensure consistency, every candle may be different</li>
      <li>Sometimes you may notice darker patches or wet spots – this is not a fault, it is just the natural way the wax has set – it does not affect the candle in any way</li>
      <li>The top of the candle may also appear slightly uneven – this is just a sign of natural soy wax being hand poured</li>
      <li>Do not leave your candle in the sunlight as it may turn a yellow colour – again this does not affect the candle in any way – it just loses its creamy white colour</li>
      <li>As these candles contain no preservatives or chemicals it is recommended that they should be used within 6 months</li>
    </ul>
  </section>

  <div class="base-rule"></div>

  <div class="brand-seal">Brume<br>d'Orvelle</div>
  <div class="range-photo" role="img" aria-label="Photo of the candle range: jars in blue, cream and black lined up on a dark surface"></div>
</main>
</body>
</html>
```